Actors Postcard Design

I need a postcard designed for me. I am an actor, voice over artist and technical adviser for tv, film and videogames. I am open to color ideas. My photos are in black and white so something to make those stand out a bit. Masculine colors like dark blue etc..I have seen some of your designs with 3 photos which I liked. Perhaps a 2-3 photo scheme. Back of postcard to contain my resume. Want it to look professional and not cartoonish (since I mentioned video games). Front to have photos and job title and contact info

Please take my color direction lightly, I am open to all color schemes. light or dark. You are the professionals. Am looking forward to seeing what all of you come up with. Thanks

Tv

```html
<!DOCTYPE html>
<html lang="en">
<head>
<meta charset="utf-8">
<title>Marek "Mark" Kowalczyk – Actor Postcard</title>
<link href="https://fonts.googleapis.com/css2?family=Questrial&family=Montserrat:wght@600;700&display=swap" rel="stylesheet">
<style>
  :root {
    --ink: #000000;
    --night: #0b0c0d;
    --accent: #19a7e6;
    --paper: #f4f4f4;
    --paper-shade: #dcdcdc;
    --text-light: #ffffff;
    --text-dark: #1d1d1d;
  }
  html, body {
    margin: 0;
    padding: 0;
    overflow: hidden;
    background: var(--ink);
  }
  .postcard {
    position: relative;
    width: 1200px;
    height: 924px;
    overflow: hidden;
    background: linear-gradient(180deg, #070808 0%, var(--ink) 100%);
    font-family: "Questrial", "Century Gothic", sans-serif;
    color: var(--text-light);
  }
  .hero-portrait {
    position: absolute;
    left: 470px;
    top: 0;
    width: 730px;
    height: 924px;
    background: radial-gradient(ellipse 46% 44% at 58% 36%, #2a2b2c 0%, #1a1b1c 45%, #0c0d0d 75%, rgba(0,0,0,0) 100%);
  }
  .snapshot {
    position: absolute;
    background: var(--paper);
    box-shadow: 6px 10px 22px rgba(0,0,0,0.7);
  }
  .snapshot--back {
    left: 60px;
    top: -160px;
    width: 540px;
    height: 660px;
    transform: rotate(-8deg);
    background: var(--paper-shade);
  }
  .snapshot--back .snapshot-photo {
    position: absolute;
    left: 22px;
    top: 22px;
    width: 496px;
    height: 520px;
    background: linear-gradient(160deg, #3b4650 0%, #20262c 100%);
  }
  .snapshot--front {
    left: 8px;
    top: 95px;
    width: 560px;
    height: 620px;
    transform: rotate(-9deg);
  }
  .snapshot--front .snapshot-photo {
    position: absolute;
    left: 22px;
    top: 22px;
    width: 516px;
    height: 470px;
    background: linear-gradient(135deg, #5f8a3a 0%, #8fae5a 35%, #3d4a2a 65%, #1c1f22 100%);
  }
  .snapshot-contact {
    position: absolute;
    left: 0;
    right: 0;
    top: 500px;
    text-align: center;
  }
  .snapshot-phone {
    display: block;
    color: var(--accent);
    font-size: 42px;
    line-height: 1.1;
  }
  .snapshot-email {
    display: block;
    color: var(--text-dark);
    font-size: 27px;
    line-height: 1.2;
  }
  .page-curl {
    position: absolute;
    right: 0;
    top: 0;
    width: 440px;
    height: 240px;
  }
  .page-curl-label {
    position: absolute;
    right: 30px;
    top: 20px;
    width: 160px;
    text-align: center;
    font-size: 29px;
    line-height: 1.2;
    color: var(--text-light);
  }
  .stats {
    position: absolute;
    left: 80px;
    top: 782px;
    display: grid;
    grid-template-columns: 245px auto;
    row-gap: 12px;
    font-size: 29px;
  }
  .stat::before {
    content: "";
    display: inline-block;
    width: 0;
    height: 0;
    border-left: 12px solid var(--accent);
    border-top: 7px solid transparent;
    border-bottom: 7px solid transparent;
    margin-right: 10px;
    vertical-align: 3px;
  }
  .stat b {
    font-family: "Montserrat", sans-serif;
    font-weight: 700;
  }
  .name {
    position: absolute;
    left: 570px;
    width: 590px;
    top: 588px;
    text-align: center;
    margin: 0;
    font-weight: normal;
  }
  .name-first, .name-last {
    display: block;
    font-size: 64px;
    letter-spacing: 2px;
    line-height: 1;
  }
  .name-nick {
    display: block;
    font-family: "Montserrat", sans-serif;
    font-weight: 700;
    color: var(--accent);
    font-size: 150px;
    line-height: 1.05;
    margin: 4px 0 2px;
    letter-spacing: -2px;
  }
</style>
</head>
<body>
<main class="postcard">
  <div class="hero-portrait" role="img" aria-label="Large dimmed black-and-white portrait of the actor"></div>

  <div class="snapshot snapshot--back">
    <div class="snapshot-photo" role="img" aria-label="Second portrait photo of the actor"></div>
  </div>

  <div class="snapshot snapshot--front">
    <div class="snapshot-photo" role="img" aria-label="Colour portrait of the actor outdoors among trees"></div>
    <div class="snapshot-contact">
      <span class="snapshot-phone">503-555-0142</span>
      <span class="snapshot-email">Markkowalczyk@mailbox.com</span>
    </div>
  </div>

  <svg class="page-curl" viewBox="0 0 440 240" aria-hidden="true">
    <defs>
      <linearGradient id="curlShade" x1="0" y1="0" x2="1" y2="1">
        <stop offset="0" stop-color="#ffffff"/>
        <stop offset="0.6" stop-color="#f2f2f2"/>
        <stop offset="1" stop-color="#bfbfbf"/>
      </linearGradient>
    </defs>
    <path d="M20 0 H440 V140 C360 120 300 90 240 60 C170 30 90 10 20 0 Z" fill="var(--accent)"/>
    <path d="M20 0 C90 10 170 30 240 60 C300 90 360 120 440 140 L440 150 L370 232 C320 180 230 90 20 0 Z" fill="url(#curlShade)"/>
  </svg>
  <div class="page-curl-label">Details on Back</div>

  <div class="stats">
    <span class="stat">Height: <b>6’0”</b></span>
    <span class="stat">Hair: <b>Blond</b></span>
    <span class="stat">Weight: <b>180</b></span>
    <span class="stat">Eyes: <b>Green</b></span>
  </div>

  <h1 class="name">
    <span class="name-first">MAREK</span>
    <span class="name-nick">“MARK”</span>
    <span class="name-last">KOWALCZYK</span>
  </h1>
</main>
</body>
</html>
```